Business Card Design

I need a business card for a new company based in Australia called "MedLinkora".

Its a cloud program for GPs that allows them to search for the specialist they require using a simple user friendly tool.

I would like the colours to match those in the program (the colours in the logo attached).

The final design should reflect the programs clarity, ease of use and professionalism.

Target Market(s)

GPs and other Health Professionals

Industry/Entity Type

Business

Contact Information for Business Card

MedLinkora; The Trusted Clinician Index; Marla Ostrove CEO; 0438215906; marla@medlinkora.example; www.medlinkora.example

Requirements
Must have
• Must have the logo attached; the web address and my name and phone number
Nice to have
• the slogan "The Trusted Clinician Index"

```html
<!DOCTYPE html>
<html lang="en">
<head>
<meta charset="utf-8">
<title>MedLinkora Business Card</title>
<link href="https://fonts.googleapis.com/css2?family=Open+Sans:wght@300;400;700&display=swap" rel="stylesheet">
<style>
  :root {
    --bg: #e9eaec;
    --navy: #123f8c;
    --royal: #1a64c0;
    --cyan: #17a9e1;
    --sky: #86d3ee;
    --paper: #ffffff;
    --ink: #333a40;
    --muted: #8a9097;
  }
  * { box-sizing: border-box; margin: 0; padding: 0; }
  html, body { width: 1200px; height: 1200px; overflow: hidden; }
  body {
    background: var(--bg);
    font-family: "Open Sans", Arial, sans-serif;
    position: relative;
  }
  .card {
    position: absolute;
    left: 250px;
    width: 700px;
    height: 400px;
    border-radius: 6px;
    overflow: hidden;
    box-shadow: 0 10px 30px rgba(0,0,0,0.12);
  }
  /* Front */
  .card-front {
    top: 150px;
    background: linear-gradient(135deg, var(--sky) 0%, #a9e0f3 100%);
  }
  .front-band {
    position: absolute;
    left: 0; top: 130px;
    width: 260px; height: 240px;
    border-radius: 0 60px 60px 0;
    background: linear-gradient(160deg, var(--cyan) 0%, var(--royal) 45%, var(--navy) 100%);
  }
  .front-panel {
    position: absolute;
    left: 110px; top: 95px;
    width: 520px; height: 210px;
    border-radius: 105px;
    background: var(--paper);
    display: flex;
    flex-direction: column;
    justify-content: center;
    padding-left: 70px;
  }
  .wordmark {
    font-weight: 300;
    color: var(--cyan);
    letter-spacing: 1px;
    line-height: 1;
  }
  .front-panel .wordmark { font-size: 62px; }
  .tagline {
    font-weight: 300;
    color: var(--muted);
    letter-spacing: 0.5px;
  }
  .front-panel .tagline { font-size: 20px; margin-top: 8px; }

  /* Back */
  .card-back {
    top: 650px;
    background: var(--paper);
  }
  .name-bar {
    position: absolute;
    left: 0; top: 50px;
    width: 330px; height: 44px;
    background: var(--cyan);
    display: flex;
    align-items: center;
    justify-content: flex-end;
    padding-right: 18px;
    color: #10222e;
    font-size: 20px;
  }
  .name-bar .name { font-weight: 700; margin-right: 6px; }
  .name-bar .role { font-size: 14px; font-weight: 400; }
  .back-brand {
    position: absolute;
    right: 40px; top: 130px;
    text-align: right;
  }
  .back-brand .wordmark { font-size: 44px; }
  .back-brand .tagline { font-size: 14px; margin-top: 6px; }
  .contact-list {
    position: absolute;
    left: 330px; top: 250px;
    list-style: none;
    color: var(--ink);
    font-size: 20px;
    letter-spacing: 0.5px;
  }
  .contact-list li {
    display: flex;
    align-items: center;
    height: 32px;
  }
  .contact-list svg {
    width: 16px; height: 16px;
    margin-right: 12px;
    fill: #555b61;
  }
</style>
</head>
<body>
  <section class="card card-front" aria-label="Business card front">
    <div class="front-band"></div>
    <div class="front-panel">
      <div class="wordmark">MedLinkora</div>
      <div class="tagline">The Trusted Clinician Index</div>
    </div>
  </section>

  <section class="card card-back" aria-label="Business card back">
    <div class="name-bar"><span class="name">Marla Ostrove</span><span class="role">CEO</span></div>
    <div class="back-brand">
      <div class="wordmark">MedLinkora</div>
      <div class="tagline">The Trusted Clinician Index</div>
    </div>
    <ul class="contact-list">
      <li>
        <svg viewBox="0 0 16 16" aria-hidden="true"><rect x="4" y="1" width="8" height="14" rx="1.5"/><rect x="5.5" y="3" width="5" height="8" fill="#fff"/></svg>
        0438215906
      </li>
      <li>
        <svg viewBox="0 0 16 16" aria-hidden="true"><rect x="1" y="3" width="14" height="10" rx="1.5"/><path d="M2 4.5 L8 9 L14 4.5" stroke="#fff" stroke-width="1.3" fill="none"/></svg>
        marla@medlinkora.example
      </li>
      <li>
        <svg viewBox="0 0 16 16" aria-hidden="true"><circle cx="8" cy="8" r="7"/><g stroke="#fff" stroke-width="1" fill="none"><ellipse cx="8" cy="8" rx="3" ry="7"/><path d="M1 8h14M2.5 4.5h11M2.5 11.5h11"/></g></svg>
        www.medlinkora.example
      </li>
    </ul>
  </section>
</body>
</html>
```